Rio Dorado Salsa – CPG Website with WordPress - Store Locator: WP Maps plugin

Larkmoor Food Company is a startup consumer packaged goods (CPG) brand launching its flagship product line — Rio Dorado Salsa. We’re seeking a talented web designer to create a bold, professional, mobile-optimized website using WordPress with a WP Maps store locator to help customers find local retailers.

Our goal is to build a strong online presence that supports both retail growth and direct-to-consumer sales.

See Rio Dorado _Website_Design_Brief word document.

The website URL is https://riodoradosalsa.example/

Target Market(s)

Consumers of gourmet salsa

Industry/Entity Type

Consumer Packaged Goods - Salsa manufacturer.

Coding

Coded - Design and coding required

Number of Pages Required

5+ page

Requirements
Must have
• The design of the Rio Dorado Salsa website shall emulate the clean, polished aesthetic of Brinvale.example.

```html
<!DOCTYPE html>
<html lang="en">
<head>
<meta charset="utf-8">
<title>Rio Dorado Salsa</title>
<link href="https://fonts.googleapis.com/css2?family=Montserrat:wght@400;500;600;700&display=swap" rel="stylesheet">
<style>
:root{
  --blush:#f3e3df;
  --brick:#b84a2e;
  --brick-deep:#a63d25;
  --panel-red:#c4482f;
  --ink:#1c1c1c;
  --muted:#555;
  --white:#fff;
  --teal:#1a9680;
}
*{box-sizing:border-box;margin:0;padding:0}
html,body{width:1200px;height:2909px;overflow:hidden}
body{position:relative;font-family:'Montserrat',sans-serif;color:var(--ink);background:var(--white)}
.abs{position:absolute}
.logo-word{font-family:'Montserrat',sans-serif;font-weight:700;color:var(--brick);display:flex;align-items:center;gap:8px}
.logo-word .dot{width:12px;height:12px;border-radius:50%;background:var(--brick)}

/* hero */
.hero{left:0;top:0;width:1200px;height:536px;background:var(--blush)}
.hero-panel{left:874px;top:0;width:326px;height:536px;background:var(--panel-red)}
.hero-art{left:598px;top:68px;width:602px;height:468px;border-radius:40px 0 0 0;
  background:radial-gradient(ellipse at 50% 55%,#d9b45a 0%,#c96a3f 40%,rgba(196,72,47,0) 75%)}
.nav a{position:absolute;top:40px;font-size:17px;color:var(--ink);text-decoration:none;font-weight:500}
.nav a.active{color:var(--brick);font-weight:600}
.btn{position:absolute;display:flex;align-items:center;justify-content:center;border-radius:30px;font-size:17px;font-weight:500;text-decoration:none}
.btn-white{background:var(--white);color:var(--brick)}
.btn-brick{background:var(--brick);color:var(--white)}
.hero h1{left:113px;top:160px;font-size:54px;font-weight:500;line-height:60px;letter-spacing:.5px}
.hero p{left:113px;top:302px;width:470px;font-size:17.5px;line-height:26px;color:#333}

/* section titles */
.section-title{left:0;width:1200px;text-align:center;font-size:40px;font-weight:600;color:var(--brick)}
.flourish{left:500px;width:200px;height:50px;border-radius:25px;background:linear-gradient(90deg,rgba(200,40,40,.15),rgba(200,40,40,.55))}

/* feature */
.product-art{left:73px;top:745px;width:582px;height:463px;border-radius:50% 50% 45% 45%;
  background:radial-gradient(ellipse at 50% 45%,#c83a2c 0%,#e0573a 35%,#f2a083 60%,rgba(255,255,255,0) 75%)}
.feature-intro{left:703px;top:794px;width:430px;font-size:16.5px;line-height:24px;color:#333}
.feature-icon{left:703px;width:79px;height:75px;border-radius:12px;background:var(--brick);display:flex;align-items:center;justify-content:center}
.feature-name{left:804px;font-size:19px;font-weight:500}
.feature-text{left:806px;width:260px;font-size:14px;line-height:21px;color:var(--muted)}

/* reviews */
.reviews-bg{left:0;top:1293px;width:1200px;height:632px;background:linear-gradient(135deg,#c4482f,#b5402a 50%,#c95438)}
.reviews-panel{left:76px;top:1508px;width:1050px;height:332px;border-radius:30px;background:var(--blush)}
.review-card{top:1552px;width:287px;height:205px;background:var(--white);border-radius:14px;padding:24px 22px}
.stars{width:108px;height:30px;background:var(--teal);display:flex;align-items:center;justify-content:center;gap:2px;margin-bottom:18px}
.review-card h3{font-size:17.5px;font-weight:500;line-height:24px;margin-bottom:12px}
.review-card p{font-size:13px;line-height:20px;color:var(--muted)}
.dots{left:0;top:1781px;width:1200px;display:flex;justify-content:center;align-items:center;gap:9px}
.dots span{width:10px;height:10px;border-radius:50%;background:#5a4a46}
.dots span.on{width:15px;height:15px;background:var(--brick)}

/* recipes */
.recipe-img{width:203px;height:205px;border-radius:14px}
.recipe-title{width:260px;font-size:18.5px;font-weight:500;line-height:26px}
.recipe-text{width:250px;font-size:13.5px;line-height:21.5px;color:var(--muted)}
.recipe-link{font-size:16px;color:var(--brick);text-decoration:underline}

/* footer */
.footer{left:0;top:2749px;width:1200px;height:160px;background:var(--blush)}
.footer-nav a{position:absolute;top:2811px;font-size:18px;color:var(--ink);text-decoration:none}
.footer-rule{left:441px;top:2851px;width:644px;height:1px;background:#555}
.copyright{right:115px;top:2870px;font-size:13.5px;color:#444}
.copyright a{color:#444}
</style>
</head>
<body>

<section class="hero abs" aria-label="Hero"></section>
<div class="hero-panel abs"></div>
<div class="hero-art abs" role="img" aria-label="Three salsa jars — habanero, verde and all natural — surrounded by red chili peppers"></div>

<div class="logo-word abs" style="left:113px;top:36px;font-size:28px">Rio Dorado</div>
<nav class="nav">
  <a class="active" href="#" style="left:333px">Home</a>
  <a href="#" style="left:415px">Product</a>
  <a href="#" style="left:511px">Receipe</a>
  <a href="#" style="left:606px">About</a>
  <a href="#" style="left:687px">Review</a>
  <a href="#" style="left:775px">Contact</a>
</nav>
<a class="btn btn-white" href="#" style="left:955px;top:32px;width:132px;height:38px">Shop Now</a>

<div class="hero">
  <h1 class="abs">Elevate Every Dish<br>With Salsa</h1>
  <p class="abs">Lorem ipsum dolor sit amet, consectetur adipiscing elit, sed do eiusmod tempor incididunt ut labore et dolore magna aliqua.</p>
</div>
<a class="btn btn-brick" href="#" style="left:113px;top:393px;width:132px;height:38px">Shop Now</a>

<!-- feature product -->
<h2 class="section-title abs" style="top:612px">Feature Product</h2>
<div class="flourish abs" style="top:666px" role="img" aria-label="Red brush swirl flourish"></div>
<div class="product-art abs" role="img" aria-label="Habanero salsa jar with a splash of red salsa"></div>
<p class="feature-intro abs">Sed ut perspiciatis unde omnis iste natus error sit voluptatem accusantium doloremque laudantium, totam rem aperiam, eaque ipsa quae ab illo inve ntore veritatis et quasi</p>

<div class="feature-icon abs" style="top:922px">
  <svg width="46" height="40" viewBox="0 0 46 40"><path d="M6 30 C18 34 32 28 36 14 L40 16 C36 34 16 40 4 34 Z" fill="#fff"/><path d="M36 14 C37 8 40 5 44 4" stroke="#fff" stroke-width="3" fill="none" stroke-linecap="round"/></svg>
</div>
<div class="feature-name abs" style="top:924px">Lorem Ipsum Dolor Sit</div>
<div class="feature-text abs" style="top:953px">Lorem ipsum dolor sit amet, conse ctetur adipiscing elit, sed</div>

<div class="feature-icon abs" style="top:1008px">
  <svg width="40" height="44" viewBox="0 0 40 44"><path d="M20 2 C26 12 32 18 32 27 A12 12 0 0 1 8 27 C8 18 14 12 20 2 Z" fill="#fff"/></svg>
</div>
<div class="feature-name abs" style="top:1010px">Lorem Ipsum Dolor Sit</div>
<div class="feature-text abs" style="top:1039px">Lorem ipsum dolor sit amet, conse ctetur adipiscing elit, sed</div>

<div class="feature-icon abs" style="top:1102px">
  <svg width="48" height="38" viewBox="0 0 48 38"><rect x="8" y="2" width="32" height="12" rx="4" fill="#fff"/><rect x="2" y="16" width="44" height="6" rx="2" fill="#fff"/><rect x="6" y="24" width="36" height="12" rx="3" fill="#fff"/></svg>
</div>
<div class="feature-name abs" style="top:1104px">Lorem Ipsum Dolor Sit</div>
<div class="feature-text abs" style="top:1133px">Lorem ipsum dolor sit amet, conse ctetur adipiscing elit, sed</div>

<!-- reviews -->
<div class="reviews-bg abs" role="img" aria-label="Soft-focus red chili peppers background"></div>
<h2 class="section-title abs" style="top:1368px;color:var(--white)">Reviews</h2>
<div class="flourish abs" style="top:1423px;background:linear-gradient(90deg,rgba(255,255,255,.25),rgba(255,255,255,.7))" role="img" aria-label="White brush swirl flourish"></div>
<div class="reviews-panel abs"></div>

<article class="review-card abs" style="left:140px">
  <div class="stars"><svg width="94" height="16" viewBox="0 0 94 16"><g fill="#fff"><path id="st" d="M8 0 L10 5.5 L16 6 L11.5 9.8 L13 16 L8 12.6 L3 16 L4.5 9.8 L0 6 L6 5.5Z"/><use href="#st" x="19"/><use href="#st" x="38"/><use href="#st" x="57"/></g><path d="M84 1 L86 6 L91.5 6.4 L87.3 9.8 L88.6 15 L84 12 L79.4 15 L80.7 9.8 L76.5 6.4 L82 6Z" fill="none" stroke="#fff" stroke-width="1.3"/></svg></div>
  <h3>Very good, and I'm a salsa snob!</h3>
  <p>Lorem ipsum dolor sit amet, consect etur adipiscing elit, sed do eiu smod tempor incididunt ...</p>
</article>
<article class="review-card abs" style="left:457px">
  <div class="stars"><svg width="94" height="16" viewBox="0 0 94 16"><g fill="#fff"><use href="#st"/><use href="#st" x="19"/><use href="#st" x="38"/><use href="#st" x="57"/></g><path d="M84 1 L86 6 L91.5 6.4 L87.3 9.8 L88.6 15 L84 12 L79.4 15 L80.7 9.8 L76.5 6.4 L82 6Z" fill="none" stroke="#fff" stroke-width="1.3"/></svg></div>
  <h3>Awesome Taste,<br>Fresh</h3>
  <p>Lorem ipsum dolor sit amet, consect etur adipiscing elit, sed do eiu smod tempor incididunt ...</p>
</article>
<article class="review-card abs" style="left:774px">
  <div class="stars"><svg width="94" height="16" viewBox="0 0 94 16"><g fill="#fff"><use href="#st"/><use href="#st" x="19"/><use href="#st" x="38"/><use href="#st" x="57"/></g><path d="M84 1 L86 6 L91.5 6.4 L87.3 9.8 L88.6 15 L84 12 L79.4 15 L80.7 9.8 L76.5 6.4 L82 6Z" fill="none" stroke="#fff" stroke-width="1.3"/></svg></div>
  <h3>At $4.79 That Is A Great Value</h3>
  <p>Lorem ipsum dolor sit amet, consect etur adipiscing elit, sed do eiu smod tempor incididunt ...</p>
</article>
<div class="dots abs"><span class="on"></span><span></span><span></span><span></span></div>

<!-- recipes -->
<h2 class="section-title abs" style="top:2005px">Our Recipes</h2>
<div class="flourish abs" style="top:2057px" role="img" aria-label="Red brush swirl flourish"></div>

<div class="recipe-img abs" style="left:113px;top:2148px;background:linear-gradient(135deg,#3a3d3c,#b3261e 50%,#4a6b2a)" role="img" aria-label="Bowl of fresh red chili peppers with basil"></div>
<div class="recipe-title abs" style="left:336px;top:2157px">Sed ut perspiciatis unde om nis iste natus error</div>
<div class="recipe-text abs" style="left:337px;top:2220px">Lorem ipsum dolor sit amet, conse ctetur adipiscing elit, sed do eius mod tempor incididunt ut labore et dolore magna aliqua.</div>
<a class="recipe-link abs" href="#" style="left:337px;top:2317px">View Details</a>

<div class="recipe-img abs" style="left:620px;top:2148px;background:linear-gradient(135deg,#8c8781,#c0281c 50%,#6b5a4a)" role="img" aria-label="Bowl of red chili sauce with peppers and chili flakes"></div>
<div class="recipe-title abs" style="left:843px;top:2157px">Sed ut perspiciatis unde om nis iste natus error</div>
<div class="recipe-text abs" style="left:844px;top:2220px">Lorem ipsum dolor sit amet, conse ctetur adipiscing elit, sed do eius mod tempor incididunt ut labore et dolore magna aliqua.</div>
<a class="recipe-link abs" href="#" style="left:844px;top:2317px">View Details</a>

<div class="recipe-img abs" style="left:113px;top:2380px;background:linear-gradient(135deg,#c0561f,#e3a45a 55%,#a8321c)" role="img" aria-label="Pepperoni pizza with peppers"></div>
<div class="recipe-title abs" style="left:336px;top:2389px">Sed ut perspiciatis unde om nis iste natus error</div>
<div class="recipe-text abs" style="left:337px;top:2452px">Lorem ipsum dolor sit amet, conse ctetur adipiscing elit, sed do eius mod tempor incididunt ut labore et dolore magna aliqua.</div>
<a class="recipe-link abs" href="#" style="left:337px;top:2549px">View Details</a>

<div class="recipe-img abs" style="left:620px;top:2380px;background:linear-gradient(135deg,#f4ece6,#e8b06a 55%,#c62f22)" role="img" aria-label="Penne pasta with a red chili pepper and basil"></div>
<div class="recipe-title abs" style="left:843px;top:2389px">Sed ut perspiciatis unde om nis iste natus error</div>
<div class="recipe-text abs" style="left:844px;top:2452px">Lorem ipsum dolor sit amet, conse ctetur adipiscing elit, sed do eius mod tempor incididunt ut labore et dolore magna aliqua.</div>
<a class="recipe-link abs" href="#" style="left:844px;top:2549px">View Details</a>

<a class="btn btn-brick" href="#" style="left:526px;top:2624px;width:149px;height:37px">View More</a>

<!-- footer -->
<footer class="footer abs"></footer>
<div class="logo-word abs" style="left:113px;top:2807px;font-size:38px">Rio Dorado</div>
<nav class="footer-nav">
  <a href="#" style="left:458px">Home</a>
  <a href="#" style="left:552px">Product</a>
  <a href="#" style="left:661px">Receipe</a>
  <a href="#" style="left:771px">About</a>
  <a href="#" style="left:864px">Review</a>
  <a href="#" style="left:966px">Contact</a>
</nav>
<span class="abs" style="left:1060px;top:2811px;width:24px;height:24px;border-radius:50%;border:2px solid var(--brick)" aria-label="Social profile"></span>
<div class="footer-rule abs"></div>
<div class="copyright abs">Copyright © 2025 Rio Dorado Salsa. All rights reserved &nbsp;|&nbsp; <a href="#">Privacy Policy</a></div>

</body>
</html>
```